We need a new website design for our company Brindle Forks (https://www.brindleforks.example/). We DO NOT WANT A BORING STANDARD SITE. This site has to be different, and has to POP!

Logo Files: https://files.example-share.net/folders/7kQwT2mZpL9xR4vB8nJc3HdYs6uFa1oE

Website Photos here: https://files.example-share.net/folders/5R-GhuK2W_pqtVnaLiEy47zmkTd83bv

Websites we like:
https://morrowind-demo.sitecraft.example/
http://plattero.example/

We will need the site building Wordpress/Woocommerce and also help with interior pages & installation plug-ins -- see further attachments.

Information about the company:
1. PURPOSE: Why do we exist?
We believe that food is the root source to healthy living.
2. VISION: What future do we want to help create?
A world of healthy and happy people.
3. MISSION: What are we here to do?
Empower every person to utilize food as a means of living a healthy life.

Value Proposition:
Brindle Forks develops new food based on the latest science to provide the human body with the proper nutrients for optimal health. Our research based foods target the key health functions that support healthy aging and active lifestyles. Since 2002, we have been innovating and designing our meals to meet the needs for healthy aging to active lifestyles. To help people perform their best, today & in the future.

Objective:
This is a nationwide issue and it's coming to the surface. Food affects people in a number of different ways. Our objective is to create an approachable and sustainable solution that can assist people with a number of ailments. The end result for all of them is feeling a feeling they haven't felt in quite some time. Feeling a refreshed you. Like water for fish, food for humans. Keep it clean and simple so you can focus on enjoying your life.

PHRASES/TAGLINES:
Empowerment Through Food
Real Food, Real Results
Nutrition Made Simple
Not Just Meal Prep, Food Science
A healthier you, delivered to your door
Increase your health and wellness baseline.
plain card shape the potential of healthier eating
Become the best version of you
It’s incredible what proper nutrition feels like
Taste & feel the difference. Your future self will thank you.
A healthier you is just a meal away
Life Changing results
Overwhelmed with being healthy, stops here.
Designed by doctors, approved by humans
Results Driven Healthy Eating, Delivered to you.
Become the person you deserve to be.
Enjoy the process of becoming a better you

Value Propositions:
We Educate & Empower People Through Food to Live Their Best Life
Sustainable health through proper nutrition… that’s enjoyable too.

Key Statements:
We provide satisfying meals that are nutrient dense & deliver results.
Our meals provide an easy way to enjoy an anti-inflammatory diet that's as satisfying as it is healthy.
Health, fat loss & feeling good through chef-prepared, nutrient-dense, satisfying meals delivered to your door.

PLEASE REVIEW THE ATTACHMENTS.

Industry/Entity Type

See Description & Attachments

Coding

Coded - Design and coding required

Number of Pages Required

5+ page

Font styles to use
Other font styles liked:
• See Description & Attachments

Colors
0094D4
00A9DD
6FCCEA
C7EBF8
E9F6FB
00AB8E
00BBA5
67D7C9
C6EFE9
E9F9F6

Requirements
Must have
Nice to have
Should not have

```html
<!DOCTYPE html>
<html lang="en">
<head>
<meta charset="utf-8">
<title>Brindle Forks — Real Food, Real Results</title>
<link rel="stylesheet" href="https://fonts.googleapis.com/css2?family=Josefin+Sans:wght@400;600;700&family=Lato:wght@400;700&display=swap">
<style>
:root{
  --green-dark:#0f4c3a;
  --green:#17614a;
  --green-deep:#0c3b2d;
  --green-light:#7fae6e;
  --mint:#e4efe1;
  --sage:#c3dfbf;
  --cream:#e9e2c9;
  --ink:#1e1e1e;
  --muted:#555;
  --white:#fff;
}
*{box-sizing:border-box;margin:0;padding:0}
html,body{width:1200px;height:4873px;overflow:hidden}
body{position:relative;font-family:"Lato",sans-serif;color:var(--ink);background:var(--white)}
.head-font{font-family:"Josefin Sans",sans-serif}
section,header,footer{position:absolute;left:0;width:1200px;overflow:hidden}
.abs{position:absolute}
.btn{position:absolute;display:flex;align-items:center;justify-content:center;background:var(--green-dark);color:var(--white);font-family:"Josefin Sans",sans-serif;font-weight:700;font-size:15px;letter-spacing:.5px;border-radius:30px}
.btn-outline{position:absolute;display:flex;align-items:center;justify-content:center;border:2px solid var(--green-dark);color:var(--green-dark);font-family:"Josefin Sans",sans-serif;font-weight:700;font-size:15px;letter-spacing:1px;border-radius:30px}

/* header */
.site-header{top:0;height:136px;background:var(--white)}
.brand{left:100px;top:40px;display:flex;align-items:center;gap:10px}
.brand-mark{width:26px;height:26px;border-radius:50%;background:var(--green)}
.brand-name{font-family:"Josefin Sans",sans-serif;font-weight:700;font-size:27px;color:var(--green)}
.brand-tag{left:100px;top:116px;font-size:10px;letter-spacing:2.5px;color:var(--green);font-weight:700}
.phone{right:100px;top:11px;font-size:13px;display:flex;align-items:center;gap:6px}
.nav{left:314px;top:62px;display:flex;gap:27px;font-size:14px;letter-spacing:.3px}
.nav a{color:var(--ink);text-decoration:none}
.nav a.active{color:var(--green-light)}
.nav-icons{left:880px;top:58px;display:flex;gap:26px}
.login{left:961px;top:49px;width:138px;height:42px;font-size:17px}

/* hero */
.hero{top:136px;height:558px;background:radial-gradient(circle at 75% 45%,#4a4a44 0%,#262624 45%,#1a1a19 100%)}
.hero-photo{left:540px;top:30px;width:640px;height:520px;border-radius:50%;background:radial-gradient(circle at 50% 55%,#9a8a3c 0%,#5b6a3a 40%,#3d4a3e 70%,rgba(40,40,38,0) 100%)}
.hero-title{left:98px;top:160px;font-family:"Josefin Sans",sans-serif;font-weight:700;font-size:74px;line-height:80px;letter-spacing:1px}
.hero-title .g{color:#1f7a55}
.hero-title .c{color:var(--cream)}
.hero-shop{left:98px;top:341px;width:156px;height:43px}
.dots{left:98px;top:463px;display:flex;gap:14px}
.dots span{width:13px;height:13px;border-radius:50%;background:#666}
.dots span:first-child{background:#ddd}

/* values */
.values{top:694px;height:468px}
.value{width:330px;text-align:center}
.value svg{display:block;margin:82px auto 0}
.value h3{font-family:"Josefin Sans",sans-serif;font-weight:600;font-size:20px;letter-spacing:1px;margin-top:24px}
.value p{font-size:15px;color:#444;line-height:22px;margin:10px auto 0;width:300px}

/* about */
.about{top:1162px;height:495px;background:var(--mint);overflow:visible}
.about h2{left:98px;top:78px;font-family:"Josefin Sans",sans-serif;font-weight:700;font-size:50px}
.about h4{left:98px;top:136px;font-family:"Josefin Sans",sans-serif;font-weight:700;font-size:21px;letter-spacing:.5px}
.about p{left:98px;top:182px;width:470px;font-size:14.5px;line-height:24px;color:#333}
.about .btn{left:98px;top:348px;width:156px;height:45px}
.plate{left:600px;top:-25px;width:560px;height:560px;border-radius:50%;background:radial-gradient(circle,#c2583a 0%,#b9482c 30%,#3f4f2c 48%,#232844 55%,#2b3154 80%,#1c2038 100%);box-shadow:0 30px 50px rgba(0,0,0,.25)}
.ring{border-radius:50%}

/* menu */
.menu{top:1657px;height:1168px}
.menu h2{left:0;width:1200px;text-align:center;top:138px;font-family:"Josefin Sans",sans-serif;font-weight:700;font-size:47px;letter-spacing:1px}
.menu-grid{left:98px;display:grid;grid-template-columns:repeat(4,242px);column-gap:12px}
.dish{position:relative;height:369px}
.dish-photo{height:172px}
.dish h3{font-family:"Josefin Sans",sans-serif;font-weight:700;font-size:19px;line-height:26px;margin-top:15px}
.dish .info{font-size:13px;color:#666;line-height:22px;margin-top:5px}
.dish .price{font-size:13.5px;font-weight:700;margin-top:6px}
.dish .btn{left:0;bottom:0;width:140px;height:38px;font-size:12.5px}
.load-more{left:515px;top:1058px;width:170px;height:46px}

/* faq */
.faq{top:2825px;height:585px;background:var(--sage)}
.faq h2{left:0;width:1200px;text-align:center;top:90px;font-family:"Josefin Sans",sans-serif;font-weight:700;font-size:50px;letter-spacing:1px}
.faq-list{left:240px;top:157px;width:721px}
.faq-item{height:48px;margin-bottom:8px;background:var(--green-dark);color:var(--white);display:flex;align-items:center;justify-content:space-between;padding:0 18px;font-size:17px;font-weight:700}
.faq .btn-outline{left:515px;top:450px;width:170px;height:46px}

/* audience */
.audience{top:3410px;height:563px;background:linear-gradient(135deg,#0f4a37 0%,#1b5a42 50%,#0e3f30 100%)}
.audience h2{left:98px;top:128px;font-family:"Josefin Sans",sans-serif;font-weight:700;font-size:48px;color:var(--white);letter-spacing:1px}
.arrows{left:1020px;top:108px;display:flex;gap:8px}
.aud-card{top:213px;width:316px;height:205px;border:1.5px solid rgba(255,255,255,.6);border-radius:12px;color:var(--white)}
.aud-photo{position:absolute;left:14px;top:42px;width:105px;height:130px;border-radius:10px}
.aud-card h3{position:absolute;left:128px;right:12px;top:14px;text-align:right;font-family:"Josefin Sans",sans-serif;font-weight:700;font-size:16.5px;letter-spacing:.5px}
.aud-card p{position:absolute;left:128px;right:12px;top:38px;font-size:13.5px;line-height:21px}

/* awards */
.awards{top:3973px;height:439px}
.awards h2{left:0;width:1200px;text-align:center;top:100px;font-family:"Josefin Sans",sans-serif;font-weight:700;font-size:46px;letter-spacing:1px}
.stat{top:198px;width:300px;text-align:center}
.stat-icon{width:66px;height:66px;margin:0 auto;border-radius:50%}
.stat strong{display:block;font-family:"Josefin Sans",sans-serif;font-weight:700;font-size:45px;margin-top:30px;line-height:45px}
.stat span{display:block;font-size:17px;color:#333;margin-top:4px;letter-spacing:.3px}

/* footer */
.site-footer{top:4412px;height:461px;background:var(--green-deep);color:#e7eee9}
.foot-col{top:121px}
.foot-col h4{font-family:"Josefin Sans",sans-serif;font-weight:700;font-size:14.5px;letter-spacing:1px;margin-bottom:22px}
.foot-col li{list-style:none;font-size:14px;height:35px;display:flex;gap:10px}
.foot-col li::before{content:"›";font-size:16px;line-height:15px}
.subscribe{left:789px;top:157px;width:312px;height:48px;background:var(--white);border-radius:26px;display:flex;align-items:center;justify-content:space-between;padding:0 20px 0 14px;color:#333;font-size:14px}
.foot-rule{left:100px;top:390px;width:1001px;height:1px;background:rgba(255,255,255,.4)}
.copyright{left:100px;top:420px;font-size:13px}
.cards{left:897px;top:414px;display:flex;gap:12px}
.cards span{width:42px;height:26px;border-radius:4px;background:#f1f1f1}
</style>
</head>
<body>

<header class="site-header">
  <div class="abs brand"><span class="brand-mark"></span><span class="brand-name">Brindle Forks</span></div>
  <div class="abs brand-tag">EAT BETTER. LIVE BETTER.</div>
  <div class="abs phone">
    <svg width="13" height="13" viewBox="0 0 24 24"><path fill="#1e1e1e" d="M6.6 10.8a15.1 15.1 0 0 0 6.6 6.6l2.2-2.2a1 1 0 0 1 1-.25 11.4 11.4 0 0 0 3.6.57 1 1 0 0 1 1 1V20a1 1 0 0 1-1 1A17 17 0 0 1 3 4a1 1 0 0 1 1-1h3.5a1 1 0 0 1 1 1c0 1.25.2 2.45.57 3.6a1 1 0 0 1-.25 1z"/></svg>
    855-010-4477
  </div>
  <nav class="abs nav">
    <a class="active" href="#">HOME</a><a href="#">SHOP NOW</a><a href="#">ABOUT</a><a href="#">MENU</a><a href="#">PROGRAMS</a><a href="#">FAQ</a>
  </nav>
  <div class="abs nav-icons">
    <svg width="18" height="17" viewBox="0 0 24 22"><path fill="#1e1e1e" d="M1 1h4l3 12h12l3-9H7" stroke="#1e1e1e" stroke-width="2" fill-opacity="0"/><path fill="#1e1e1e" d="M7 4h16l-3 9H8z"/><circle cx="9" cy="18" r="2" fill="#1e1e1e"/><circle cx="19" cy="18" r="2" fill="#1e1e1e"/></svg>
    <svg width="16" height="16" viewBox="0 0 24 24"><circle cx="10" cy="10" r="7" fill="none" stroke="#1e1e1e" stroke-width="3"/><path d="M15 15l7 7" stroke="#1e1e1e" stroke-width="3"/></svg>
  </div>
  <div class="btn login">LOGIN</div>
</header>

<section class="hero">
  <div class="abs hero-photo" role="img" aria-label="Bowl of roasted vegetable and grain meal on a dark plate"></div>
  <h1 class="abs hero-title"><span class="g">Real</span> <span class="c">Food,</span><br><span class="c">Real</span> <span class="g">Results</span></h1>
  <div class="btn hero-shop">SHOP NOW</div>
  <div class="abs dots"><span></span><span></span><span></span></div>
</section>

<section class="values">
  <div class="abs value" style="left:75px">
    <svg width="160" height="110" viewBox="0 0 160 110" role="img" aria-label="Target illustration on a green shape"><path fill="#0f4c3a" d="M20 40C22 12 60 2 95 4c40 3 62 22 60 52-2 34-28 52-68 50C45 104 17 78 20 40z"/></svg>
    <h3>PURPOSE</h3>
    <p>We believe that food is the root source to healthy living.</p>
  </div>
  <div class="abs value" style="left:435px">
    <svg width="160" height="110" viewBox="0 0 160 110" role="img" aria-label="Light bulb illustration on a green shape"><path fill="#0f4c3a" d="M8 50C6 20 40 4 80 6c42 2 72 16 72 48 0 32-30 50-74 50C36 104 10 82 8 50z"/></svg>
    <h3>VISION</h3>
    <p>A world of healthy and happy people.</p>
  </div>
  <div class="abs value" style="left:795px">
    <svg width="160" height="110" viewBox="0 0 160 110" role="img" aria-label="Flag illustration on a green shape"><path fill="#0f4c3a" d="M6 44C8 14 44 2 84 4c44 3 68 26 66 56-2 30-26 46-66 44C38 102 4 78 6 44z"/></svg>
    <h3>MISSION</h3>
    <p>Empower every person to utilize food as a means of living a healthy life.</p>
  </div>
</section>

<section class="about">
  <div class="abs ring" style="left:-30px;top:45px;width:56px;height:56px;border:8px solid var(--green-dark)"></div>
  <div class="abs ring" style="left:565px;top:50px;width:18px;height:18px;border:2.5px solid var(--green-dark)"></div>
  <div class="abs ring" style="left:1126px;top:426px;width:11px;height:11px;border:2px solid var(--green-dark)"></div>
  <h2 class="abs">About</h2>
  <h4 class="abs">Value Proposition</h4>
  <p class="abs">Brindle Forks develops new food based on the latest science to provide the human body with the proper nutrients for optimal health. Our research based foods target the key health functions that support healthy aging and active lifestyles. Since 2002, we have been innovating and designing our meals to meet the needs for healthy aging to active lifestyles.</p>
  <div class="btn">READ MORE</div>
  <div class="abs plate" role="img" aria-label="Plate of seasoned ground turkey with cauliflower and herbs"></div>
</section>

<section class="menu">
  <h2 class="abs">Our Menu</h2>
  <div class="abs menu-grid" style="top:207px">
    <article class="dish"><div class="dish-photo" role="img" aria-label="Chicken quinoa bowl" style="background:linear-gradient(135deg,#b9a58a,#7d8a5e)"></div><h3>Chicken quinoa bowl</h3><p class="info">Cal 477 | gluten free | no antibiotics | no hormones | all natural</p><p class="price">$13.00</p><div class="btn">ADD TO CART</div></article>
    <article class="dish"><div class="dish-photo" role="img" aria-label="Chocolate almond oats in jars" style="background:linear-gradient(135deg,#8a6a4a,#3d2c22)"></div><h3>Chocolate almond oats</h3><p class="info">Cal 353 | gluten free | no antibiotics| no hormones | all natural</p><p class="price">$ 6.50</p><div class="btn">ADD TO CART</div></article>
    <article class="dish"><div class="dish-photo" role="img" aria-label="Blueberry almond oats in jars" style="background:linear-gradient(135deg,#c9b89a,#5a5a62)"></div><h3>Blueberry almond oats</h3><p class="info">Cal 331 | gluten free | no antibiotics | no hormones | all natural</p><p class="price">$13.00</p><div class="btn">ADD TO CART</div></article>
    <article class="dish"><div class="dish-photo" role="img" aria-label="Chicken greek salad" style="background:linear-gradient(135deg,#c8b296,#4f7a3a)"></div><h3>Chicken greek salad</h3><p class="info">Cal 312 | gluten free | no antibiotics | no hormones | all natural</p><p class="price">$12.50</p><div class="btn">ADD TO CART</div></article>
  </div>
  <div class="abs menu-grid" style="top:631px">
    <article class="dish"><div class="dish-photo" role="img" aria-label="Spinach and feta stuffed chicken" style="background:linear-gradient(135deg,#6b5a3e,#2e3a22)"></div><h3>Spinach and feta stuffed chicken</h3><p class="info">Cal 611 | gluten free | no antibiotics no hormones | all natural</p><p class="price">$13.00</p><div class="btn">ADD TO CART</div></article>
    <article class="dish"><div class="dish-photo" role="img" aria-label="Chicken blueberry goat cheese salad" style="background:linear-gradient(135deg,#8a8a5a,#3a4a2a)"></div><h3>Chicken blueberry goat cheese salad</h3><p class="info">Cal 296 | gluten free | low carb antioxidant rich</p><p class="price">$13.00</p><div class="btn">ADD TO CART</div></article>
    <article class="dish"><div class="dish-photo" role="img" aria-label="Mediterranean tuna salad" style="background:linear-gradient(135deg,#d8c7a8,#b0453a)"></div><h3>Mediterranean tuna</h3><p class="info">Cal 177 | gluten free | low carb low calorie</p><p class="price">$13.00</p><div class="btn">ADD TO CART</div></article>
    <article class="dish"><div class="dish-photo" role="img" aria-label="Turkey with roasted vegetables" style="background:linear-gradient(135deg,#a8452e,#3a5a2a)"></div><h3>Turkey Tips</h3><p class="info">Cal 283 | paleo | low carb | keto gluten free</p><p class="price">$12.50</p><div class="btn">ADD TO CART</div></article>
  </div>
  <div class="btn-outline load-more">LOAD MORE</div>
</section>

<section class="faq">
  <div class="abs ring" style="left:1158px;top:100px;width:70px;height:70px;border:8px solid var(--green-dark)"></div>
  <h2 class="abs">Frequently Asked Questions</h2>
  <div class="abs faq-list">
    <div class="faq-item"><span>Q. What is Brindle Forks?</span><svg width="20" height="20" viewBox="0 0 20 20"><circle cx="10" cy="10" r="9" fill="#fff"/><path d="M8 6l4 4-4 4" stroke="#0f4c3a" stroke-width="2.4" fill="none"/></svg></div>
    <div class="faq-item"><span>Q. Can I customize my order?</span><svg width="20" height="20" viewBox="0 0 20 20"><circle cx="10" cy="10" r="9" fill="#fff"/><path d="M8 6l4 4-4 4" stroke="#0f4c3a" stroke-width="2.4" fill="none"/></svg></div>
    <div class="faq-item"><span>Q. Do you have gluten free options?</span><svg width="20" height="20" viewBox="0 0 20 20"><circle cx="10" cy="10" r="9" fill="#fff"/><path d="M8 6l4 4-4 4" stroke="#0f4c3a" stroke-width="2.4" fill="none"/></svg></div>
    <div class="faq-item"><span>Q. Why pre-order online?</span><svg width="20" height="20" viewBox="0 0 20 20"><circle cx="10" cy="10" r="9" fill="#fff"/><path d="M8 6l4 4-4 4" stroke="#0f4c3a" stroke-width="2.4" fill="none"/></svg></div>
    <div class="faq-item"><span>Q. What is the window for ordering?</span><svg width="20" height="20" viewBox="0 0 20 20"><circle cx="10" cy="10" r="9" fill="#fff"/><path d="M8 6l4 4-4 4" stroke="#0f4c3a" stroke-width="2.4" fill="none"/></svg></div>
  </div>
  <div class="btn-outline">VIEW ALL</div>
</section>

<section class="audience">
  <div class="abs ring" style="left:164px;top:-18px;width:42px;height:42px;border:6px solid var(--green-deep)"></div>
  <h2 class="abs">Who is Brindle Forks For?</h2>
  <div class="abs arrows">
    <svg width="38" height="38" viewBox="0 0 38 38"><circle cx="19" cy="19" r="17" fill="none" stroke="#c3dfbf" stroke-width="1.5"/><path d="M22 12l-7 7 7 7" stroke="#c3dfbf" stroke-width="1.5" fill="none"/></svg>
    <svg width="38" height="38" viewBox="0 0 38 38"><circle cx="19" cy="19" r="18" fill="#c3dfbf"/><path d="M16 12l7 7-7 7" stroke="#0f4c3a" stroke-width="1.5" fill="none"/></svg>
  </div>
  <div class="abs aud-card" style="left:98px"><div class="aud-photo" role="img" aria-label="Meal container with turkey and vegetables" style="background:linear-gradient(135deg,#c0532f,#2a2a2a)"></div><h3>General Health</h3><p>You need the support of a healthy diet to get back in shape and improve your overall health. Having a meal plan that supports you would benefit you.</p></div>
  <div class="abs aud-card" style="left:441px"><div class="aud-photo" role="img" aria-label="Plate of turkey with cauliflower" style="background:radial-gradient(circle,#c2583a 0%,#2b3154 60%,rgba(0,0,0,0) 72%)"></div><h3>Business Individuals</h3><p>You have a growing to-do list that never seems to end. No time to do healthy meal prep. You prefer a healthy meal over a fast food diet.</p></div>
  <div class="abs aud-card" style="left:783px"><div class="aud-photo" role="img" aria-label="Meal prep containers with colourful vegetables" style="background:linear-gradient(135deg,#d0a23a,#5a2a4a)"></div><h3>Fitness Enthusiasts</h3><p>You eat clean, fitness &amp; eating right are a huge part of your life. Enjoy healthy meal delivery to keep yourself on track.</p></div>
</section>

<section class="awards">
  <h2 class="abs">Award Winning Meals</h2>
  <div class="abs stat" style="left:16px"><div class="stat-icon" role="img" aria-label="Happy client icon" style="background:#f5c518"></div><strong>150K</strong><span>HAPPY CLIENTS</span></div>
  <div class="abs stat" style="left:314px"><div class="stat-icon" role="img" aria-label="Serving cloche icon" style="background:#f4a61e"></div><strong>500K</strong><span>MEALS SERVED NATION WIDE</span></div>
  <div class="abs stat" style="left:643px"><div class="stat-icon" role="img" aria-label="Chef icon" style="background:#e9e4dc"></div><strong>35+</strong><span>CHEF PREPARED MEALS</span></div>
  <div class="abs stat" style="left:883px"><div class="stat-icon" role="img" aria-label="Trophy icon" style="background:#f2b51c"></div><strong>215</strong><span>AWARDS</span></div>
</section>

<footer class="site-footer">
  <div class="abs foot-col" style="left:100px"><h4>MY ACCOUNT</h4><ul><li>Site Help</li><li>About Us</li><li>Contact Us</li><li>Shipping &amp; Returns</li><li>All Products</li><li>Gift Certificates</li></ul></div>
  <div class="abs foot-col" style="left:341px"><h4>VIEW CART</h4><ul><li>About Us</li><li>Corporate Catering</li><li>Podcast</li><li>Become an Affiliate</li></ul></div>
  <div class="abs foot-col" style="left:581px"><h4>ORDER STATUS</h4><ul><li>Contact Us</li><li>Privacy Policy</li><li>Testimonials</li></ul></div>
  <div class="abs foot-col" style="left:789px"><h4>STAY IN THE LOOP</h4></div>
  <div class="abs subscribe"><span>Enter email address</span><svg width="16" height="16" viewBox="0 0 24 24"><path fill="#0f4c3a" d="M2 12L22 3l-6 19-4-8z"/></svg></div>
  <div class="abs foot-rule"></div>
  <div class="abs copyright">© 2022 <strong>Brindle Forks</strong>. All right reserved</div>
  <div class="abs cards" aria-label="Accepted payment methods"><span></span><span></span><span></span><span></span></div>
</footer>

</body>
</html>
```